Emerging Ed-Tech Startup seeking Stationery Designs!

We are in need of basic set of stationery designs to be used for our business operations, letters, emails, and in-office materials. We are a technology startup enhancing on campus work experience offerings by establishing a collaborative work environment for the completion of such tasks.

Our colors are Vibrant Tiffany Blue/Black/White.

Website: www.scholarhorizonhub.com (Still under construction aside from the landing pages)

Please make sure the designs use a brighter more vibrant tiffany blue color than seen in the image files uploaded. We are not using those materials.

Our logo has been added as a file as well, please use that for any designs (include that logo). Thank you.

```html
<!DOCTYPE html>
<html lang="en">
<head>
<meta charset="utf-8">
<title>ScholarHorizon – Presentation Folder</title>
<link href="https://fonts.googleapis.com/css2?family=Montserrat:wght@400&display=swap" rel="stylesheet">
<style>
  :root {
    --tiffany: #2fc6d4;
    --tiffany-soft: #d9eff5;
    --slate: #6d6e70;
    --ink: #1b1b1b;
    --paper: #ffffff;
    --trim: #5a5a5c;
  }
  html, body {
    margin: 0;
    padding: 0;
    width: 864px;
    height: 1200px;
    overflow: hidden;
    background: var(--paper);
  }
  .folder-sheet {
    display: block;
    width: 864px;
    height: 1200px;
  }
  .trim-line { fill: none; stroke: var(--trim); stroke-width: 0.8; }
  .spine-outer { fill: var(--slate); }
  .band-slate { fill: var(--slate); }
  .cover-artwork { fill: url(#coverArtTone); }
  .brand-mark { fill: var(--tiffany); }
  .brand-name {
    font-family: "Montserrat", sans-serif;
    font-weight: 400;
    font-size: 13px;
    fill: var(--ink);
    letter-spacing: 0.3px;
  }
  .contact-line {
    font-family: "Montserrat", sans-serif;
    font-weight: 400;
    font-size: 4.6px;
    fill: var(--slate);
  }
  .contact-line .contact-web { fill: var(--tiffany); }
</style>
</head>
<body>
<svg class="folder-sheet" viewBox="0 0 823 1143" xmlns="http://www.w3.org/2000/svg" aria-label="Presentation folder, outside and inside spreads">
  <defs>
    <linearGradient id="coverArtTone" x1="0" y1="0" x2="1" y2="0">
      <stop offset="0" stop-color="#d9eff5"/>
      <stop offset="0.6" stop-color="#a9dde6"/>
      <stop offset="1" stop-color="#7f9ea5"/>
    </linearGradient>
  </defs>

  <!-- Outside spread -->
  <g class="outside-spread">
    <rect class="trim-line" x="0.5" y="0.5" width="395.5" height="562"/>
    <rect class="spine-outer" x="396" y="0.5" width="31" height="562"/>
    <rect class="trim-line" x="427" y="0.5" width="395.5" height="562"/>

    <text class="contact-line" x="22" y="538">Suite # 2-14 &#160;|&#160; Lake Avenue &#160;|&#160; +00 12 3456789 &#160;|&#160; info@scholarhorizonhub.com &#160;|&#160; <tspan class="contact-web">www.scholarhorizonhub.com</tspan></text>

    <g class="brand">
      <rect class="brand-mark" x="474" y="42" width="42" height="42"/>
      <text class="brand-name" x="528" y="68">ScholarHorizon</text>
    </g>

    <polygon class="cover-artwork" role="img" aria-label="Geometric cover artwork in tiffany blue and slate tones"
      points="427,518 500,505 600,505 700,520 823,395 823,563 427,563"/>
  </g>

  <!-- Inside spread -->
  <g class="inside-spread">
    <rect class="trim-line" x="0.5" y="580.5" width="395.5" height="562"/>
    <rect class="trim-line" x="396" y="580.5" width="31" height="562"/>
    <rect class="trim-line" x="427" y="580.5" width="395.5" height="562"/>
    <polygon class="band-slate" points="427,1048 823,958 823,1143 427,1143"/>
  </g>
</svg>
</body>
</html>
```